Process Serving Company needs a letterhead design

Looking to have a letterhead designed for letters to attorneys advertising our business. We would like something eye catching but professional. Colors and logos are attached. Please add "Process Service and Attorney Support" near the logo or header

Target Market(s)

Attorneys

Font styles to use
Serif
Sans Serif

Colors
33a6d7
0255a3
85cae6
cee9f5
ecf7fb

```html
<!DOCTYPE html>
<html lang="en">
<head>
<meta charset="utf-8">
<title>Mesa Ridge Serve – Letterhead</title>
<link href="https://fonts.googleapis.com/css2?family=Open+Sans:wght@400;600&family=Roboto+Condensed:wght@700&display=swap" rel="stylesheet">
<style>
  :root {
    --brand-blue: #0a8fd0;
    --brand-navy: #0255a3;
    --band-blue: #0d95d3;
    --ink: #3a3a3a;
    --ink-dark: #1e1e1e;
    --paper: #ffffff;
    --backdrop: #e9ecef;
  }
  * { margin: 0; padding: 0; box-sizing: border-box; }
  html, body {
    width: 1040px; height: 1200px; overflow: hidden;
    background: var(--backdrop);
    font-family: "Open Sans", Arial, sans-serif;
    color: var(--ink);
  }
  .letterhead {
    position: absolute; left: 53px; top: 0;
    width: 933px; height: 1200px;
    background: var(--paper);
  }
  .brand {
    position: absolute; left: 0; right: 0; top: 34px;
    display: flex; justify-content: center; align-items: center; gap: 12px;
  }
  .brand-mark {
    width: 18px; height: 18px; background: var(--brand-blue);
  }
  .brand-name {
    font-weight: 600; font-size: 34px; letter-spacing: 0.5px;
    color: var(--brand-blue); text-transform: uppercase; line-height: 1;
  }
  .tagline-row {
    position: absolute; left: 87px; width: 752px; top: 110px;
    display: flex; align-items: center; gap: 12px;
  }
  .tagline-rule { flex: 1; height: 2px; background: var(--brand-blue); }
  .tagline {
    font-family: "Roboto Condensed", "Arial Narrow", sans-serif;
    font-weight: 700; font-size: 15px; color: var(--ink-dark);
    text-transform: uppercase; white-space: nowrap;
  }
  .letter {
    position: absolute; left: 87px; top: 216px; width: 755px;
    font-size: 15px; line-height: 18px;
  }
  .issue-date { margin-bottom: 18px; }
  .recipient { margin-bottom: 50px; }
  .salutation { margin-bottom: 33px; }
  .body-copy p {
    font-size: 14.6px; letter-spacing: -0.1px;
    line-height: 27px; text-align: justify; hyphens: auto;
    margin-bottom: 27px;
  }
  .closing { margin-top: 58px; }
  .signatory {
    margin-top: 62px; font-size: 19px; font-weight: 600; color: var(--ink-dark);
  }
  .signatory-title { margin-top: 10px; font-size: 15px; }
  .footer-address {
    position: absolute; left: 0; right: 0; top: 1120px;
    text-align: center; font-size: 18px; color: var(--ink-dark);
  }
  .contact-band {
    position: absolute; left: 0; right: 0; bottom: 0; height: 48px;
    background: var(--band-blue); color: #fff;
    display: flex; justify-content: center; align-items: center;
    font-size: 18px;
  }
  .contact-band strong { font-weight: 600; }
</style>
</head>
<body>
  <main class="letterhead">
    <header>
      <div class="brand">
        <span class="brand-mark"></span>
        <span class="brand-name">Mesa Ridge Serve</span>
      </div>
      <div class="tagline-row">
        <span class="tagline-rule"></span>
        <span class="tagline">Process Service and Attorney Support</span>
        <span class="tagline-rule"></span>
      </div>
    </header>

    <section class="letter" lang="en">
      <p class="issue-date">Issuing Date: May 5, 2018</p>
      <p class="recipient">Name Of Employee Mr. XYZABC<br>Address of Employee<br>Address Line 2 etc..</p>
      <p class="salutation">Dear Mr.XYZABC</p>
      <div class="body-copy">
        <p>Lorem Ipsum has been the industry's standard dummy text ever since the 1500s, when an unknown printer took a galley of type and scrambled it to make a type specimen book. It has survived not only five centuries, but also the leap into electronic typesetting, remaining essentially unchanged. It was popularised in the 1960s with the release of Typeline sheets containing Lorem Ipsum passages, and more recently with desktop publishing software like Quillpress Layout including versions of Lorem Ipsum.</p>
        <p>Lorem Ipsum is simply dummy text of the printing and typesetting industry. Lorem Ipsum has been the industry's standard dummy text ever since the 1500s, when an unknown printer took a galley of type and scrambled it to make a type specimen book.</p>
        <p>It has survived not only five centuries, but also the leap into electronic typesetting, remaining essentially unchanged. It was popularised in the 1960s with the release of Typeline sheets containing Lorem IpsumIpsum passages.</p>
      </div>
      <p class="closing">Yours Sincerely</p>
      <p class="signatory">Daniel Harper</p>
      <p class="signatory-title">Managing Director</p>
    </section>

    <footer>
      <p class="footer-address">4210 E Canyon Vista Rd #204, Tempe AZ 85281</p>
      <p class="contact-band">
        <strong>Phone:</strong>&nbsp;480-555-0142 &nbsp;|&nbsp; <strong>Fax:</strong>&nbsp;480-555-0187 &nbsp;|&nbsp; www.MesaRidgeServe.com &nbsp;|&nbsp; Info@MesaRidgeServe.com
      </p>
    </footer>
  </main>
</body>
</html>
```